Film Studio Desires Beautiful Movie Poster Design

We are looking for a Movie Poster design for the first film from Brindle Harbor Studios. It is a Short Film titled WINTER LANTERN. Winter Lantern is a story being told by a father to his dying daughter in the hospital. It's about an elderly couple and their Magical encounter with a little girl in a cemetery. The final design should communicate the thought of remembering lost loved ones, cherishing those we have and hinting slightly to a Heavenly/Magical element. The story mostly takes place in a Cemetery. Part of the story it is lightly snowing. Added Photos are screen shots from the film. (Open to all of your great ideas, however, versions centered around the Angel Statue and or the picture with the 3 people walking might be interesting. Maybe even a Headstone that reads WINTER LANTERN??)
The poster needs to say: "Dalen Fitzwater's" above the title "Winter Lantern". It should also say the line "Sometimes Something Happens..." and "A Brindle Harbor Studios Production" somewhere in the design. (These can be smaller fonts of course) This design needs to be very professional. This will be used as both a standard print 27″ x 40″ Poster and a Hi-Res file to send out. Thank You Very Much!
Updates
The poster needs to say: "Dalen Fitzwater's" above the title "Winter Lantern". It should also say the line "Sometimes Something Happens..." and "A Brindle Harbor Studios Production" somewhere in the design. (These can be smaller fonts of course)
Target Market(s)
Target Customers are Film Festival attendees and Film Executives. All Ages.
Industry/Entity Type
Movie
Look and feel

```html
<!DOCTYPE html>
<html lang="en">
<head>
<meta charset="utf-8">
<title>Winter Lantern — Poster</title>
<link href="https://fonts.googleapis.com/css2?family=Yanone+Kaffeesatz:wght@400;500&family=Kaushan+Script&family=Open+Sans:wght@700&display=swap" rel="stylesheet">
<style>
  :root {
    --page: #ffffff;
    --plum: #55303f;
    --ink: #5a2b3f;
    --parchment-light: #f1dcb6;
    --parchment-mid: #e6c998;
    --parchment-dark: #d9b27e;
    --mat: #f8c8d0;
    --still-sky: #c9c6b8;
    --still-branches: #8f8a6e;
    --still-coats: #9b8474;
    --still-blush: #c9a3a0;
    --still-path: #7e6a56;
  }
  html, body {
    margin: 0;
    width: 1200px;
    height: 900px;
    overflow: hidden;
    background: var(--page);
  }
  .canvas {
    position: relative;
    width: 1200px;
    height: 900px;
  }
  .poster {
    position: absolute;
    left: 297px;
    top: 0;
    width: 606px;
    height: 900px;
    background: var(--plum);
  }
  .parchment {
    position: absolute;
    left: 28px;
    top: 28px;
    width: 555px;
    height: 844px;
    background: radial-gradient(ellipse at 50% 45%, var(--parchment-light) 0%, var(--parchment-mid) 60%, var(--parchment-dark) 100%);
  }
  .tagline {
    position: absolute;
    top: 34px;
    left: 0;
    width: 100%;
    margin: 0;
    text-align: center;
    font-family: "Yanone Kaffeesatz", sans-serif;
    font-weight: 500;
    font-size: 38px;
    color: var(--ink);
  }
  .mat {
    position: absolute;
    left: 48px;
    top: 89px;
    width: 452px;
    height: 500px;
    background: var(--mat);
    box-shadow: 4px 5px 6px rgba(70, 40, 30, 0.35);
  }
  .still {
    position: absolute;
    left: 40px;
    top: 35px;
    width: 374px;
    height: 430px;
    background:
      radial-gradient(ellipse 40% 30% at 50% 62%, var(--still-blush) 0%, rgba(201,163,160,0) 100%),
      radial-gradient(ellipse 70% 25% at 40% 8%, var(--still-sky) 0%, rgba(201,198,184,0) 100%),
      linear-gradient(180deg, var(--still-branches) 0%, var(--still-coats) 45%, var(--still-coats) 70%, var(--still-path) 100%);
    box-shadow: 0 0 12px 8px var(--mat) inset;
  }
  .credit {
    position: absolute;
    top: 606px;
    left: 0;
    width: 100%;
    text-align: center;
    color: var(--ink);
  }
  .credit-block {
    display: inline-block;
    text-align: right;
  }
  .credit-name {
    margin: 0;
    font-family: "Yanone Kaffeesatz", sans-serif;
    font-weight: 500;
    font-size: 46px;
    line-height: 1;
  }
  .credit-format {
    margin: 0;
    font-family: "Yanone Kaffeesatz", sans-serif;
    font-weight: 500;
    font-size: 26px;
    line-height: 1;
  }
  .title {
    position: absolute;
    top: 650px;
    left: 0;
    width: 100%;
    margin: 0;
    font-family: "Kaushan Script", cursive;
    font-weight: 400;
    font-size: 76px;
    line-height: 1;
    color: var(--ink);
  }
  .title-first,
  .title-second {
    display: block;
    text-align: center;
  }
  .title-first { padding-right: 150px; }
  .title-second { padding-left: 130px; margin-top: -16px; }
  .studio {
    position: absolute;
    bottom: 10px;
    left: 0;
    width: 100%;
    margin: 0;
    text-align: center;
    font-family: "Open Sans", sans-serif;
    font-weight: 700;
    font-size: 14px;
    color: var(--ink);
  }
</style>
</head>
<body>
<main class="canvas">
  <article class="poster">
    <div class="parchment">
      <p class="tagline">Sometimes Something Happens...</p>
      <div class="mat">
        <div class="still" role="img" aria-label="Film still: an elderly couple walking hand in hand with a little girl in a pink coat along a cemetery path in light snow, a stone angel statue beside them"></div>
      </div>
      <div class="credit">
        <div class="credit-block">
          <p class="credit-name">Dalen Fitzwater’s</p>
          <p class="credit-format">short film</p>
        </div>
      </div>
      <h1 class="title"><span class="title-first">Winter</span><span class="title-second">Lantern</span></h1>
      <p class="studio">A Brindle Harbor Studios Production</p>
    </div>
  </article>
</main>
</body>
</html>
```